Cobbleford Works New Website

Custom Wood Cabinetry and Precisions Wood Cutting website. I have created a pdf document with all the specs for the project and attached it. I am just typing stuff in here so it stops telling me my description is too short. Their once was a man from Nantucket.. he used to pee in a bucket.. roses are red, cardinals are birds, i wish they didn't require 300 words.
Number of Pages Required
1 page

```html
<!DOCTYPE html>
<html lang="en">
<head>
<meta charset="utf-8">
<title>Cobbleford Works — Custom Cabinetry &amp; CNC Wood Cutting</title>
<link href="https://fonts.googleapis.com/css2?family=Roboto:wght@400;500;700&family=Roboto+Slab:wght@600;700&display=swap" rel="stylesheet">
<style>
:root{
  --accent:#c8a27a;
  --accent-dark:#a9825a;
  --ink:#2d2d2d;
  --muted:#7b7b7b;
  --band:#f1f0ee;
  --white:#ffffff;
  --brand-bg:#2a1f16;
}
*{box-sizing:border-box;margin:0;padding:0}
html,body{width:1200px;height:3312px;overflow:hidden}
body{font-family:"Roboto",Arial,sans-serif;color:var(--ink);background:var(--white);position:relative}
.abs{position:absolute}
.photo{position:absolute;display:block}

/* hero */
.hero{position:absolute;left:0;top:0;width:1200px;height:620px;overflow:hidden}
.hero-shade{position:absolute;inset:0;background:rgba(30,22,15,.45)}
.nav{position:absolute;top:0;left:0;width:1200px;height:60px;font-size:13px;color:var(--white)}
.nav-left{position:absolute;left:150px;top:20px;display:flex;gap:32px}
.nav-right{position:absolute;left:690px;top:20px;display:flex;gap:22px;align-items:center;white-space:nowrap}
.nav a{color:var(--white);text-decoration:none}
.brand{position:absolute;left:552px;top:0;width:96px;height:72px;background:var(--brand-bg);display:flex;align-items:center;justify-content:center;text-align:center;font-family:"Roboto",sans-serif;font-weight:700;font-size:13px;line-height:1.2;color:var(--accent);padding:6px}
.hero h1{position:absolute;top:140px;left:0;width:1200px;text-align:center;font-family:"Roboto Slab",Georgia,serif;font-weight:700;font-size:64px;line-height:76px;color:var(--white)}
.hero-sub{position:absolute;top:326px;left:300px;width:600px;text-align:center;font-size:13.5px;line-height:20px;color:var(--white)}
.btn{display:inline-block;background:var(--accent);color:var(--white);font-size:13px;font-weight:500;text-align:center;border-radius:3px}
.hero .btn{position:absolute;left:524px;top:436px;width:152px;height:42px;line-height:42px;font-size:15px}

/* headings */
.section-title{position:absolute;left:0;width:1200px;text-align:center;font-weight:700;font-size:32px;letter-spacing:.5px;color:var(--accent);text-transform:uppercase}
.section-sub{position:absolute;left:250px;width:700px;text-align:center;font-size:13px;color:var(--muted)}
.left-title{position:absolute;font-weight:700;font-size:32px;color:var(--accent);text-transform:uppercase}
.body-text{position:absolute;font-size:14px;line-height:23px;color:var(--muted)}
.rule{position:absolute;height:2px;background:var(--accent)}

/* about */
.about-photo{left:148px;top:680px;width:392px;height:400px;background:linear-gradient(180deg,#f2f0ec 0,#e8e4de 55%,#c9a173 56%,#b88b5b 100%);box-shadow:0 6px 16px rgba(0,0,0,.12)}

/* carousels */
.arrow{position:absolute;width:22px;height:22px}
.tile{position:absolute;width:200px;height:258px}

/* services band */
.band{position:absolute;left:0;top:1700px;width:1200px;height:500px;background:var(--band)}
.service{position:absolute;top:1876px;width:284px;height:232px}
.service .photo{left:0;top:0;width:284px;height:232px}
.service-label{position:absolute;left:24px;bottom:0;width:236px;height:58px;background:var(--white);padding:12px 14px}
.service-label b{display:block;font-size:13px;font-weight:500;color:var(--ink)}
.service-label span{display:flex;justify-content:space-between;font-size:11px;color:var(--muted);margin-top:6px}
.service-label em{font-style:normal}

/* creations */
.item{position:absolute;top:2890px;width:204px}
.item .photo{position:relative;width:204px;height:260px}
.item-name{font-size:12.5px;color:var(--accent-dark);margin-top:14px;line-height:17px}
.item-price{font-size:12.5px;color:var(--muted);margin-top:10px}
</style>
</head>
<body>

<header class="hero">
  <div class="photo" role="img" aria-label="Modern kitchen interior with white cabinets and wooden stools" style="inset:0;background:linear-gradient(160deg,#4d3c2d,#9c7e61 55%,#6a533f)"></div>
  <div class="hero-shade"></div>
  <nav class="nav">
    <div class="nav-left">
      <a href="#">Home</a><a href="#">About Us</a><a href="#">FAQs</a><a href="#">Services ▾</a><a href="#">Contact Us</a>
    </div>
    <div class="brand">Cobbleford Works</div>
    <div class="nav-right">
      <span>&#9990; +1 555 014 8220</span>
      <span>&#9993; hello@cobblefordworks.com</span>
      <svg width="14" height="14" viewBox="0 0 14 14"><circle cx="6" cy="6" r="4.5" fill="none" stroke="#fff" stroke-width="1.6"/><path d="M9.5 9.5L13 13" stroke="#fff" stroke-width="1.6"/></svg>
      <svg width="16" height="14" viewBox="0 0 16 14"><path d="M1 1h2.5l2 8h8l1.5-6H4.3" fill="none" stroke="#fff" stroke-width="1.5"/><circle cx="6.5" cy="12" r="1.2" fill="#fff"/><circle cx="12.5" cy="12" r="1.2" fill="#fff"/></svg>
    </div>
  </nav>
  <h1>Live with design<br>&amp; Innovation</h1>
  <p class="hero-sub">Lorem ipsum dolor sit amet, consectetur adipiscing elit, sed do eiusmod tempor incididunt ut labore et dolore magna aliqua. Ut enim ad minim veniam, quis nostrud exercitation ullamco laboris.</p>
  <span class="btn">Get a Quote</span>
</header>
<svg class="abs" style="left:0;top:560px" width="1200" height="70" viewBox="0 0 1200 70" preserveAspectRatio="none">
  <path d="M0 24 L40 30 L80 20 L130 34 L180 22 L240 36 L300 26 L360 38 L420 24 L480 34 L540 22 L600 36 L660 26 L720 38 L780 24 L840 34 L900 22 L960 36 L1020 26 L1080 34 L1140 22 L1200 30 L1200 70 L0 70Z" fill="#fff"/>
</svg>

<!-- About -->
<div class="photo about-photo" role="img" aria-label="Oak sideboard with plant against a white wall"></div>
<h2 class="left-title" style="left:640px;top:716px">About Us</h2>
<div class="rule" style="left:640px;top:762px;width:60px"></div>
<p class="body-text" style="left:640px;top:790px;width:420px">Lorem ipsum dolor sit amet, consectetur adipiscing elit, sed do eiusmod tempor incididunt ut labore et dolore magna aliqua. Ut enim ad minim veniam, quis nostrud exercitation ullamco laboris nisi ut aliquip ex ea commodo consequat. Duis aute irure dolor in reprehenderit in voluptate velit esse cillum dolore.</p>
<p class="body-text" style="left:640px;top:940px;width:420px">Ut enim ad minim in reprehenderit in voluptate velit esse cillum dolore eu fugiat nulla pariatur. Excepteur sint occaecat cupidatat non proident, sunt in culpa qui officia deserunt mollit anim id est laborum. Sed ut perspiciatis unde omnis iste natus.</p>

<!-- Custom cabinetry -->
<h2 class="section-title" style="top:1210px">Custom Cabinetry</h2>
<p class="section-sub" style="top:1278px">Lorem ipsum dolor sit amet, consectetur adipiscing elit, sed do eiusmod tempor incididunt ut labore et dolore magna aliqua.</p>
<svg class="arrow" style="left:86px;top:1452px" viewBox="0 0 22 22"><path d="M14 4L7 11l7 7" fill="none" stroke="#555" stroke-width="2"/></svg>
<svg class="arrow" style="left:1094px;top:1452px" viewBox="0 0 22 22"><path d="M8 4l7 7-7 7" fill="none" stroke="#555" stroke-width="2"/></svg>
<div class="photo tile" style="left:148px;top:1336px;background:linear-gradient(160deg,#6b4a2e,#a6774b)" role="img" aria-label="Walnut kitchen island with cabinetry"></div>
<div class="photo tile" style="left:380px;top:1336px;background:linear-gradient(160deg,#d9d2c8,#8c5f3a)" role="img" aria-label="Wooden bar counter with shelving"></div>
<div class="photo tile" style="left:616px;top:1336px;background:linear-gradient(160deg,#eef0ef,#2f6b63 70%)" role="img" aria-label="Teal kitchen cabinets with white counter"></div>
<div class="photo tile" style="left:852px;top:1336px;background:linear-gradient(160deg,#c3955d,#8a5c34)" role="img" aria-label="Rustic wooden cart with drawers"></div>
<span class="btn abs" style="left:540px;top:1634px;width:120px;height:34px;line-height:34px">Get a Quote</span>

<!-- Services -->
<div class="band"></div>
<svg class="abs" style="left:0;top:1690px" width="1200" height="24" viewBox="0 0 1200 24" preserveAspectRatio="none"><path d="M0 12 L60 6 L120 14 L200 4 L280 12 L360 6 L440 14 L520 5 L600 12 L680 6 L760 14 L840 5 L920 12 L1000 6 L1080 14 L1200 8 L1200 24 L0 24Z" fill="var(--band)"/></svg>
<svg class="abs" style="left:0;top:2190px" width="1200" height="24" viewBox="0 0 1200 24" preserveAspectRatio="none"><path d="M0 0 L1200 0 L1200 12 L1120 18 L1040 8 L960 16 L880 6 L800 16 L720 8 L640 18 L560 8 L480 16 L400 6 L320 16 L240 8 L160 18 L80 8 L0 14Z" fill="var(--band)"/></svg>
<h2 class="section-title" style="top:1784px">Our Services</h2>
<div class="service" style="left:148px">
  <div class="photo" role="img" aria-label="Dresser with framed art in a bright room" style="background:linear-gradient(160deg,#efe7df,#b98b66)"></div>
  <div class="service-label"><b>Custom Cabinets</b><span><em>Lorem ipsum dolor sit</em><em>More →</em></span></div>
</div>
<div class="service" style="left:458px">
  <div class="photo" role="img" aria-label="CNC router machine in a workshop" style="background:linear-gradient(160deg,#3f5e86,#9aa3ad)"></div>
  <div class="service-label"><b>CNC Precision Wood Cutting</b><span><em>Lorem ipsum dolor sit</em><em>More →</em></span></div>
</div>
<div class="service" style="left:768px">
  <div class="photo" role="img" aria-label="Carved decorative wood panel" style="background:linear-gradient(160deg,#7a4a2a,#b07a4c)"></div>
  <div class="service-label"><b>Custom Wood Art Projects</b><span><em>Lorem ipsum dolor sit</em><em>More →</em></span></div>
</div>

<!-- CNC -->
<h2 class="left-title" style="left:148px;top:2300px;font-size:28px;line-height:38px">CNC Precision Wood<br>Cutting</h2>
<div class="rule" style="left:148px;top:2388px;width:60px"></div>
<p class="body-text" style="left:148px;top:2408px;width:440px">Lorem ipsum dolor sit amet, consectetur adipiscing elit, sed do eiusmod tempor incididunt ut labore et dolore magna aliqua. Ut enim ad minim veniam, quis nostrud exercitation ullamco laboris nisi ut aliquip ex ea commodo.</p>
<p class="body-text" style="left:148px;top:2520px;width:440px">Duis aute irure dolor in reprehenderit in voluptate velit esse cillum dolore eu fugiat nulla pariatur sint occaecat.</p>
<span class="btn abs" style="left:148px;top:2588px;width:124px;height:34px;line-height:34px">Read More</span>
<div class="photo" style="left:652px;top:2270px;width:396px;height:404px;background:linear-gradient(160deg,#d7d3cc,#8e8a83);box-shadow:0 6px 16px rgba(0,0,0,.15)" role="img" aria-label="Plywood dinosaur skeleton model in a workshop"></div>
<div class="abs" style="left:612px;top:2620px;width:30px;height:30px;background:#fff;box-shadow:0 1px 4px rgba(0,0,0,.2)"><svg width="30" height="30" viewBox="0 0 30 30"><path d="M18 9l-6 6 6 6" fill="none" stroke="#555" stroke-width="2"/></svg></div>
<div class="abs" style="left:646px;top:2620px;width:30px;height:30px;background:#fff;box-shadow:0 1px 4px rgba(0,0,0,.2)"><svg width="30" height="30" viewBox="0 0 30 30"><path d="M12 9l6 6-6 6" fill="none" stroke="#555" stroke-width="2"/></svg></div>

<!-- Newest creations -->
<h2 class="section-title" style="top:2764px">Newest Creations</h2>
<p class="section-sub" style="top:2832px">Lorem ipsum dolor sit amet, consectetur adipiscing elit, sed do eiusmod tempor incididunt ut labore et dolore magna aliqua.</p>
<svg class="arrow" style="left:86px;top:3010px" viewBox="0 0 22 22"><path d="M14 4L7 11l7 7" fill="none" stroke="#555" stroke-width="2"/></svg>
<svg class="arrow" style="left:1094px;top:3010px" viewBox="0 0 22 22"><path d="M8 4l7 7-7 7" fill="none" stroke="#555" stroke-width="2"/></svg>
<div class="item" style="left:148px">
  <div class="photo" role="img" aria-label="Dark wood wall shelf cabinet" style="background:linear-gradient(160deg,#5a3a22,#8d6039)"></div>
  <p class="item-name">Lorem ipsum dolor sit</p><p class="item-price">$00</p>
</div>
<div class="item" style="left:382px">
  <div class="photo" role="img" aria-label="Wooden church pew bench" style="background:linear-gradient(160deg,#e2ddd5,#6d4427 60%)"></div>
  <p class="item-name">Lorem ipsum dolor amet<br>tempor</p><p class="item-price">$00</p>
</div>
<div class="item" style="left:616px">
  <div class="photo" role="img" aria-label="Carved wooden sign plaque" style="background:linear-gradient(160deg,#c9a06c,#8a5b33)"></div>
  <p class="item-name">Lorem ipsum dolor sit<br>magna</p><p class="item-price">$00</p>
  <span class="btn" style="display:block;width:204px;height:36px;line-height:36px;margin-top:18px">Shop Now</span>
</div>
<div class="item" style="left:850px">
  <div class="photo" role="img" aria-label="Plywood dinosaur model on display" style="background:linear-gradient(160deg,#d8d4cc,#a58e70)"></div>
  <p class="item-name">Lorem ipsum dolor amet<br>magna</p><p class="item-price">$00</p>
</div>

</body>
</html>
```